Modern Skincare Product Label with Logo (please look at uploaded pics)

We need a product label and logo for a skincare line. We are looking for a design for 1 tall skinny container and 1 layout that works for short wide jar containers.

Our containers are white and silver plastic.

The dimensions of the label for the tall skinny container is about 3 1/2 in wide by 3 6/8 inches tall. That is what we want designed for.

Our product line is called Lumen Skincare. We are looking for more modern design. Please try a design with lumen in bold and going vertical down the product as well as looking at the uploaded pics we posted and getting creative with them.

We are attaching product inspirations and also our blank containers.

Target Market(s)

We are looking for something gender neutral (but slightly leaning more toward targeting women).

Industry/Entity Type

Skin Care Product

Font styles to use
Sans Serif

Colors

Designer to choose colors to be used in the design.

Requirements
Must have
• We prefer a logo and packaging that is modern, simple. The background must be white. We will have about 6 different skincare categories (categories like, acne, anti-aging, normal skin, etc). We'd like that splash of color to indicate which product category it is. accent colors: bright turquoise or Orange. can have grey and black letters. modern.
• Must have a place for a barcode, ingredients list, and any other things that we're supposed to have on a label.
Nice to have
• I'm attaching pictures we like. We are targeting more high end younger crowd.
Should not have
• No clip art or typical "spa" images or outlines of a face incorporated into the logo (we think that's super cheesy). modern and sleek design. I don't like the LS in the logo.

```html
<!DOCTYPE html>
<html lang="en">
<head>
<meta charset="UTF-8">
<title>Lumen Skincare — Moisturizer Label</title>
<link rel="stylesheet" href="https://fonts.googleapis.com/css2?family=Montserrat:wght@400;500;600&display=swap">
<style>
  :root {
    --canvas-bg: #ffffff;
    --label-bg: #ffffff;
    --label-edge: #e2e2e2;
    --brand-grey: #9a9a9a;
    --accent-turquoise: #1ee3e0;
    --ink-black: #1a1a1a;
    --ink-dark: #333333;
  }
  * { margin: 0; padding: 0; box-sizing: border-box; }
  html, body {
    width: 1200px;
    height: 1000px;
    overflow: hidden;
    background: var(--canvas-bg);
    font-family: "Montserrat", sans-serif;
  }
  .canvas {
    position: relative;
    width: 1200px;
    height: 1000px;
  }
  .label {
    position: absolute;
    left: 300px;
    top: 398px;
    width: 490px;
    height: 152px;
    background: var(--label-bg);
    border: 1px solid var(--label-edge);
    overflow: hidden;
  }
  .brand {
    position: absolute;
    left: 2px;
    top: 80px;
    white-space: nowrap;
    font-weight: 500;
    font-size: 70px;
    line-height: 1;
    letter-spacing: -4px;
    color: var(--brand-grey);
  }
  .brand-dot {
    display: inline-block;
    width: 11px;
    height: 11px;
    margin-left: 8px;
    border-radius: 50%;
    background: var(--accent-turquoise);
    vertical-align: baseline;
  }
  .volume {
    position: absolute;
    right: 34px;
    top: 10px;
    font-size: 8px;
    font-weight: 600;
    color: var(--ink-black);
  }
  .category {
    position: absolute;
    left: 235px;
    top: 72px;
    width: 113px;
    font-size: 19px;
    font-weight: 400;
    color: var(--ink-dark);
    padding-bottom: 4px;
    border-bottom: 1px solid var(--accent-turquoise);
    line-height: 1.1;
  }
  .description {
    position: absolute;
    left: 235px;
    top: 105px;
    font-size: 8.5px;
    font-weight: 600;
    line-height: 12.5px;
    color: var(--ink-black);
  }
</style>
</head>
<body>
  <main class="canvas">
    <section class="label">
      <div class="brand"><span class="brand-name">lumen</span><span class="brand-dot" aria-hidden="true"></span></div>
      <p class="volume">4oz(120ml)</p>
      <h2 class="category">skin care</h2>
      <p class="description">
        hydrating and brightening<br>
        anti-oxidant moisturizer<br>
        rich in vit. c
      </p>
    </section>
  </main>
</body>
</html>
```